Business Card Design

I need a business card design for a new company that is based in Singapore region. The name of the company is called " Kalvaro Holdings Pte.Ltd " This company serves as a holding company that owns several types of businesses under our name. One of the established company in Singapore is the Kalvaro Food Industries that serves as a food service industry that has their own brand name which operates in malls and CBD areas. We would prefer the design of the business cards will use the colors of black as the base and red as for the designs. The final design of the name card should be able to communicate young and professional type of business culture. In which we appreciate creativity to their highest point.
Industry/Entity Type
Industry
Contact Information for Business Card
Matteo Bastian Kalvaro
Director, Founder
Contact: +65 81247760
E-mail: matteobk@quellmail.com

```html
<!DOCTYPE html>
<html lang="en">
<head>
<meta charset="utf-8">
<title>Kalvaro Enterprise – Business Card</title>
<link rel="stylesheet" href="https://fonts.googleapis.com/css2?family=Titillium+Web:ital,wght@0,300;0,400;0,600;1,300;1,400&display=swap">
<style>
  :root {
    --page-bg: #8a8a8a;
    --card-black: #111111;
    --card-edge: #1c1c1c;
    --brand-red: #e2352a;
    --text-white: #f4f4f4;
    --text-grey: #5c5c5c;
    --decor-grey: #1a1a1a;
  }
  * { box-sizing: border-box; margin: 0; padding: 0; }
  html, body {
    width: 1200px; height: 1000px; overflow: hidden;
    background: var(--page-bg);
    font-family: "Titillium Web", sans-serif;
  }
  .sheet {
    position: relative; width: 1200px; height: 1000px;
    display: flex; flex-direction: column; align-items: center; justify-content: center; gap: 60px;
  }
  .card {
    position: relative; width: 600px; height: 360px;
    background: var(--card-black);
    border: 1px solid var(--card-edge);
    overflow: hidden;
    box-shadow: 0 10px 30px rgba(0,0,0,0.35);
  }
  .decor-circle {
    position: absolute; border-radius: 50%;
    border: 14px solid var(--decor-grey);
  }
  .card-back .decor-circle { width: 300px; height: 300px; left: 40px; top: -10px; }
  .card-front .decor-circle { width: 220px; height: 220px; left: 330px; top: 200px; }

  .brand {
    position: absolute; display: flex; align-items: center; gap: 8px;
  }
  .brand-dot {
    border-radius: 50%; border: 3px solid var(--brand-red); flex: none;
  }
  .brand-name {
    color: var(--brand-red); font-weight: 600; text-transform: uppercase; letter-spacing: 0.06em;
  }
  .card-back .brand { right: 60px; top: 150px; }
  .card-back .brand-dot { width: 40px; height: 40px; }
  .card-back .brand-name { font-size: 19px; }
  .card-front .brand { right: 36px; top: 46px; }
  .card-front .brand-dot { width: 26px; height: 26px; border-width: 2px; }
  .card-front .brand-name { font-size: 13px; }

  .name-band { position: absolute; left: 0; top: 130px; width: 380px; height: 60px; }
  .person-name {
    position: absolute; left: 118px; top: 140px; width: 250px;
    color: var(--text-white); font-size: 23px; font-weight: 300; white-space: nowrap;
  }
  .person-role {
    position: absolute; left: 150px; top: 196px;
    color: var(--text-white); font-size: 17px; font-weight: 300; font-style: italic;
  }
  .contact {
    position: absolute; left: 384px; top: 188px;
    display: flex; gap: 12px; align-items: stretch;
  }
  .contact-divider { width: 3px; background: var(--brand-red); }
  .contact-list { list-style: none; color: var(--text-white); font-size: 13px; line-height: 20px; }
  .contact-list li { display: flex; align-items: center; gap: 7px; }
  .contact-list svg { width: 11px; height: 11px; fill: var(--text-grey); flex: none; }
</style>
</head>
<body>
<main class="sheet">

  <section class="card card-back" aria-label="Card back">
    <div class="decor-circle" aria-hidden="true"></div>
    <div class="brand">
      <span class="brand-dot" aria-hidden="true"></span>
      <span class="brand-name">Kalvaro Enterprise</span>
    </div>
  </section>

  <section class="card card-front" aria-label="Card front">
    <div class="decor-circle" aria-hidden="true"></div>
    <div class="brand">
      <span class="brand-dot" aria-hidden="true"></span>
      <span class="brand-name">Kalvaro Enterprise</span>
    </div>

    <svg class="name-band" viewBox="0 0 380 60" aria-hidden="true">
      <path d="M0 18 H96 Q100 18 100 14 V14 Q100 8 106 8 H362 Q372 8 372 18 V44 Q372 54 362 54 H106 Q100 54 100 48 Q100 44 96 44 H0 Z" fill="var(--brand-red)"/>
    </svg>
    <h1 class="person-name">Matteo Bastian Kalvaro</h1>
    <p class="person-role">Director, Founder</p>

    <div class="contact">
      <span class="contact-divider" aria-hidden="true"></span>
      <ul class="contact-list">
        <li>
          <svg viewBox="0 0 24 24" aria-hidden="true"><path d="M6.6 10.8a15.1 15.1 0 0 0 6.6 6.6l2.2-2.2a1 1 0 0 1 1-.25 11.4 11.4 0 0 0 3.6.57 1 1 0 0 1 1 1V20a1 1 0 0 1-1 1A17 17 0 0 1 3 4a1 1 0 0 1 1-1h3.5a1 1 0 0 1 1 1c0 1.25.2 2.45.57 3.57a1 1 0 0 1-.25 1z"/></svg>
          +65 81247760
        </li>
        <li>
          <svg viewBox="0 0 24 24" aria-hidden="true"><path d="M2 5h20v14H2z M2 5l10 8 10-8" /></svg>
          matteobk@quellmail.com
        </li>
      </ul>
    </div>
  </section>

</main>
</body>
</html>
```